Steadfast Support! Virtual Assistant business needs a Website

I have started an online business called "Steadfast Support". I offer all the same types of services as a typical Personal Assistant, only remotely. For example, document formatting and editing (word, powerpoint, excel etc.), email and calendar management, appointments and bookings, document creation, reports, travel and event management and so on.

I already have a logo ready to go, however I have yet to finalise the copy for the site, so if you could create the pages with pictures, and I can fill in the wording at a later date.

Target Market(s)

Anyone who is overloaded at work and needs someone to take the admin work off their hands.

Number of Pages Required

4 page

Font styles to use
Sans Serif
Script
Other font styles liked:
• Gotham Medium is used in my font

Colors

Designer to choose colors to be used in the design.

Requirements
Must have
• Home Page
• About Page
• Pricing Page
• Contact Page
Nice to have
• Pictures and a professional design, I like white space and simple design.
Should not have
• cartoons or anything unprofessional looking.

```html
<!DOCTYPE html>
<html lang="en">
<head>
<meta charset="utf-8">
<title>Steadfast Support</title>
<link href="https://fonts.googleapis.com/css2?family=Lato:wght@300;400;700&display=swap" rel="stylesheet">
<style>
  :root {
    --blue: #1f63a8;
    --blue-deep: #1a4aa0;
    --blue-light: #2a78b8;
    --ink: #2b2b2b;
    --text: #666;
    --band: #f8f8f8;
    --white: #fff;
  }
  * { box-sizing: border-box; margin: 0; padding: 0; }
  html, body { width: 1200px; height: 1110px; overflow: hidden; }
  body { font-family: "Lato", Arial, sans-serif; background: var(--white); color: var(--ink); position: relative; }

  .hero { position: absolute; left: 0; top: 0; width: 1200px; height: 420px; overflow: hidden; }
  .hero-photo { position: absolute; inset: 0; background: radial-gradient(ellipse at 60% 40%, #707378 0%, #55585d 45%, #3c3e42 100%); }
  .hero-accent { position: absolute; inset: 0; }

  .brand { position: absolute; display: flex; align-items: center; gap: 8px; font-weight: 700; font-size: 19px; letter-spacing: 0.5px; }
  .brand-dot { width: 30px; height: 30px; border-radius: 50%; }
  .brand--light { color: var(--white); }
  .brand--light .brand-dot { background: var(--white); }
  .brand--blue { color: var(--blue); }
  .brand--blue .brand-dot { background: var(--blue); }

  .nav { position: absolute; top: 36px; display: flex; font-size: 10.5px; text-transform: uppercase; }
  .nav a { position: absolute; white-space: nowrap; text-decoration: none; color: inherit; }
  .nav--top { color: var(--white); left: 0; }
  .nav a.active::after { content: ""; position: absolute; left: 0; bottom: -5px; width: 18px; height: 2px; background: var(--blue-light); }
  .phone { position: absolute; left: 890px; top: 35px; color: var(--white); font-size: 10.5px; font-weight: 700; display: flex; align-items: center; gap: 5px; }

  .hero-title { position: absolute; left: 212px; top: 140px; color: var(--white); font-weight: 300; font-size: 27px; line-height: 33px; }
  .hero-title strong { font-weight: 700; }
  .hero-text { position: absolute; left: 212px; top: 228px; width: 395px; color: #e6e6e6; font-size: 9.5px; line-height: 13.5px; font-weight: 300; }
  .hero-button { position: absolute; left: 210px; top: 294px; width: 134px; height: 29px; border: 1px solid var(--white); border-radius: 15px; color: var(--white); font-size: 11.5px; font-weight: 300; display: flex; align-items: center; justify-content: center; }

  .assistant-photo { position: absolute; left: 668px; top: 112px; width: 260px; height: 360px; border-radius: 120px 120px 40px 40px; background: linear-gradient(180deg, #c9a58c 0%, #f1dcd6 35%, #e8e8ea 55%, #4a6f9c 80%, #3b5f8c 100%); }

  .intro-brand { left: 210px; top: 490px; font-size: 17px; }
  .intro-title { position: absolute; left: 211px; top: 520px; font-size: 26px; font-weight: 300; line-height: 33px; color: var(--ink); }
  .intro-text { position: absolute; left: 213px; top: 610px; width: 340px; font-size: 9.5px; line-height: 17px; color: var(--text); font-weight: 300; }

  .stat { position: absolute; top: 550px; display: flex; align-items: center; gap: 10px; }
  .stat-ring { position: relative; width: 88px; height: 88px; }
  .stat-ring span { position: absolute; inset: 0; display: flex; align-items: center; justify-content: center; font-size: 20px; font-weight: 300; color: var(--ink); }
  .stat-label { font-size: 10.5px; line-height: 13.5px; color: var(--text); font-weight: 300; }

  .testimonials { position: absolute; left: 0; top: 748px; width: 1200px; height: 270px; background: var(--band); text-align: center; }
  .section-tag { position: absolute; left: 0; right: 0; top: 41px; font-size: 14.5px; font-weight: 700; color: var(--blue); }
  .section-title { position: absolute; left: 0; right: 0; top: 57px; font-size: 26px; font-weight: 300; color: var(--ink); }
  .quote { position: absolute; left: 268px; width: 664px; top: 116px; font-size: 12px; line-height: 22px; color: var(--text); font-weight: 300; }
  .dots { position: absolute; left: 577px; top: 226px; display: flex; gap: 8px; }
  .dots i { width: 10px; height: 10px; border-radius: 50%; background: var(--blue); display: block; }
  .dots i:first-child { background: #555; }

  .footer-brand { left: 212px; top: 1041px; }
  .nav--footer { color: #444; top: 1051px; left: 0; }
</style>
</head>
<body>
  <header class="hero">
    <div class="hero-photo" role="img" aria-label="Grey-toned photo of a man working at a laptop in an office"></div>
    <svg class="hero-accent" width="1200" height="420" viewBox="0 0 1200 420" aria-hidden="true">
      <defs>
        <linearGradient id="accent" x1="0" y1="0" x2="0" y2="1">
          <stop offset="0" stop-color="#2670ad"/>
          <stop offset="1" stop-color="#1a49a2"/>
        </linearGradient>
      </defs>
      <polygon points="864,0 1200,0 1200,420 760,420" fill="url(#accent)"/>
    </svg>

    <div class="brand brand--light" style="left:210px;top:24px;"><span class="brand-dot"></span>Steadfast Support</div>

    <nav class="nav nav--top">
      <a class="active" style="left:544px;">Home</a>
      <a style="left:596px;">Services</a>
      <a style="left:662px;">About us</a>
      <a style="left:733px;">Pricing</a>
      <a style="left:793px;">Contact</a>
    </nav>
    <div class="phone">
      <svg width="9" height="9" viewBox="0 0 24 24" aria-hidden="true"><path fill="#fff" d="M6.6 10.8c1.4 2.8 3.8 5.1 6.6 6.6l2.2-2.2c.3-.3.7-.4 1-.2 1.1.4 2.3.6 3.6.6.6 0 1 .4 1 1V20c0 .6-.4 1-1 1C10.6 21 3 13.4 3 4c0-.6.4-1 1-1h3.5c.6 0 1 .4 1 1 0 1.3.2 2.5.6 3.6.1.3 0 .7-.2 1L6.6 10.8z"/></svg>
      000-000-000
    </div>

    <h1 class="hero-title">It’s time for <strong>Steadfast Support</strong>,<br>we are everything you need.</h1>
    <p class="hero-text">We are the best Steadfast Support in the market. We provide an integral service, we work in document formatting and editing, email and calendar management, appointments and bookings, document creation, reports, travel and event management and so on.</p>
    <div class="hero-button">Lets start Now!</div>
  </header>

  <div class="assistant-photo" role="img" aria-label="Photo of a smiling assistant sitting cross-legged with a laptop, pointing to the side"></div>

  <section class="intro">
    <div class="brand brand--blue intro-brand">Steadfast Support</div>
    <h2 class="intro-title">We make the difference, we<br>organize your time &amp; life.</h2>
    <p class="intro-text">Lorem ipsum dolor sit amet, consectetuer adipiscing elit. Aenean commodo ligula eget dolor. Aenean massa. Cum sociis natoque penatibus et magnis dis parturient montes, nascetur ridiculus mus. Donec quam felis, ultricies nec, pellentesque eu, pretium quis, sem. Nulla consequat massa quis enim. Donec pede justo, frin.</p>

    <div class="stat" style="left:594px;">
      <div class="stat-ring">
        <svg width="88" height="88" viewBox="0 0 88 88" aria-hidden="true">
          <circle cx="44" cy="44" r="41" fill="none" stroke="var(--blue)" stroke-width="3" stroke-dasharray="162 258" transform="rotate(-150 44 44)"/>
        </svg>
        <span>63%</span>
      </div>
      <p class="stat-label">Lorem ipsum<br>dolor sitameat</p>
    </div>

    <div class="stat" style="left:792px;">
      <div class="stat-ring">
        <svg width="88" height="88" viewBox="0 0 88 88" aria-hidden="true">
          <circle cx="44" cy="44" r="41" fill="none" stroke="var(--blue)" stroke-width="3" stroke-dasharray="234 258" transform="rotate(-70 44 44)"/>
        </svg>
        <span>91%</span>
      </div>
      <p class="stat-label">Lorem ipsum<br>dolor sitameat</p>
    </div>
  </section>

  <section class="testimonials">
    <p class="section-tag">TESTIMONIALS</p>
    <h2 class="section-title">See what others are saying</h2>
    <p class="quote">Lorem ipsum dolor sit amet, consectetuer adipiscing elit. Aenean commodo ligula eget dolor. Aenean massa. Cum sociis natoque penatibus et magnis dis parturient montes, nascetur ridiculus mus. Donec quam felis, ultricies nec, pellentesque eu, pretium quis, sem. Nulla consequat massa quis enim. Donec pede justo, frin.</p>
    <div class="dots"><i></i><i></i><i></i></div>
  </section>

  <footer>
    <div class="brand brand--blue footer-brand"><span class="brand-dot"></span>Steadfast Support</div>
    <nav class="nav nav--footer">
      <a style="left:692px;">Home</a>
      <a style="left:745px;">Services</a>
      <a style="left:810px;">About us</a>
      <a style="left:881px;">Pricing</a>
      <a style="left:942px;">Contact</a>
    </nav>
  </footer>
</body>
</html>
```